Concrete Finishing business needs new business card and a logo design

We are a family owned and operated, concrete finishing business. 2020 marks our 33 rd year in business. We operate under Harold M. Ferrick and Sons Concrete Contractors Ltd. Harold M was my father and founder of the company. We usually shorten the name and use H M Ferrick & Sons Ltd. Most people in the Concrete Finishing industry tend to know us by our last name 'Ferrick' . in honour of our father, we would still like to have his name on the cards and logo but are open to shortening it to H.M (maybe in a small font with the W on top of the J ) and focusing more on the "Ferrick & Sons."....Or maybe something with just the initials HMF...or if you could use the "J" and somehow incorporate an artistic drawing/shape of a 'power trowel' (what we use apply a smooth finish to the concrete with) but still visually see that its a J, would be cool. Would like to see designs using Black with silver or grey lettering but are open to other ideas. Seen a business card online with the front of the business card looking like concrete and with just the word CONCRETE on it... On the back was the company name , address and contact info of the company....looked really good! i clicked doubled sided in case of something like that but we are open to just single sided as well. After viewing some of the designs, maybe a pop of colour would be nice ... open to any ideas and colours.😊

Target Market(s)

Construction

```html
<!DOCTYPE html>
<html lang="en">
<head>
<meta charset="utf-8">
<title>H M Ferrick &amp; Sons Ltd. – Business Card</title>
<link rel="stylesheet" href="https://fonts.googleapis.com/css2?family=Poppins:ital,wght@0,400;0,500;1,400&family=Saira:wght@800&display=swap">
<style>
  :root {
    --backdrop: #2b2e34;
    --card-white: #ececec;
    --card-grey: #d9d9d9;
    --concrete-light: #d8d3cc;
    --concrete-mid: #c7bfb4;
    --ink: #161616;
    --ink-soft: #3a3a3a;
    --accent-red: #d71f26;
    --photo-sky: #b9c4cf;
    --photo-yellow: #c8b23a;
    --photo-green: #6f8b4a;
    --photo-concrete: #8e939a;
    --photo-concrete-dark: #5f646b;
  }
  * { box-sizing: border-box; margin: 0; padding: 0; }
  html, body {
    width: 1200px; height: 900px; overflow: hidden;
    background: var(--backdrop);
  }
  .canvas {
    position: relative; width: 1200px; height: 900px;
  }
  .card {
    position: absolute; width: 525px; height: 300px;
    overflow: hidden; border-radius: 3px;
    box-shadow: 0 14px 30px rgba(0,0,0,.45);
  }

  /* Back side: contact details */
  .card--back { left: 50px; top: 300px; background: var(--card-white); }
  .card-back__art { position: absolute; inset: 0; }
  .card-back__brand {
    position: absolute; left: 150px; top: 28px;
    font-family: "Saira", sans-serif; font-weight: 800;
    font-size: 52px; letter-spacing: 2px; color: var(--ink);
    display: flex; align-items: center; gap: 10px;
  }
  .card-back__brand .brand-square {
    width: 14px; height: 14px; background: var(--ink);
  }
  .contact-list {
    position: absolute; left: 22px; top: 118px;
    list-style: none;
    font-family: "Poppins", sans-serif; font-size: 13px;
    color: var(--ink-soft); line-height: 22px;
  }
  .contact-list li { display: flex; align-items: center; gap: 8px; }
  .contact-list .icon { width: 14px; height: 14px; flex: none; }
  .contact-list .address-line { padding-left: 22px; }

  /* Front side: company name */
  .card--front {
    left: 625px; top: 300px;
    background: radial-gradient(ellipse at 50% 45%, var(--concrete-light), var(--concrete-mid));
  }
  .card-front__brand {
    position: absolute; left: 0; right: 0; top: 52px; text-align: center;
    font-family: "Saira", sans-serif; font-weight: 800;
    font-size: 64px; letter-spacing: 4px; color: var(--ink);
  }
  .card-front__name {
    position: absolute; left: 0; right: 0; top: 148px; text-align: center;
    font-family: "Saira", sans-serif; font-weight: 800;
    font-size: 27px; letter-spacing: 1px; color: var(--ink);
  }
  .card-front__rule {
    position: absolute; top: 166px; width: 40px; height: 1px; background: var(--ink);
  }
  .card-front__rule--left { left: 28px; }
  .card-front__rule--right { right: 28px; }
  .card-front__trade {
    position: absolute; left: 0; right: 0; top: 186px; text-align: center;
    font-family: "Poppins", sans-serif; font-weight: 500;
    font-size: 15px; letter-spacing: 2px; color: var(--ink);
  }
  .card-front__tagline {
    position: absolute; left: 0; right: 0; top: 210px; text-align: center;
    font-family: "Poppins", sans-serif; font-style: italic;
    font-size: 12px; color: var(--accent-red);
  }
</style>
</head>
<body>
<main class="canvas">

  <section class="card card--back" aria-label="Card back with contact details">
    <svg class="card-back__art" viewBox="0 0 525 300" width="525" height="300">
      <defs>
        <linearGradient id="site-photo-top" x1="0" y1="0" x2="1" y2="1">
          <stop offset="0" stop-color="var(--photo-sky)"/>
          <stop offset=".5" stop-color="var(--photo-yellow)"/>
          <stop offset="1" stop-color="var(--photo-green)"/>
        </linearGradient>
        <linearGradient id="site-photo-bottom" x1="0" y1="0" x2="1" y2="1">
          <stop offset="0" stop-color="var(--photo-concrete)"/>
          <stop offset="1" stop-color="var(--photo-concrete-dark)"/>
        </linearGradient>
      </defs>
      <polygon points="300,0 525,0 525,200 215,300 160,300" fill="var(--card-grey)"/>
      <polygon points="330,0 525,0 525,120 290,195" fill="url(#site-photo-top)"
               role="img" aria-label="Photo of a power trowel finishing fresh concrete on site"/>
      <polygon points="290,195 525,120 525,135 195,235" fill="var(--accent-red)"/>
      <polygon points="195,235 525,135 525,300 160,300" fill="url(#site-photo-bottom)"
               role="img" aria-label="Photo of a power trowel on a smooth concrete floor"/>
    </svg>

    <div class="card-back__brand"><span>HMF</span><span class="brand-square"></span></div>

    <ul class="contact-list">
      <li>
        <svg class="icon" viewBox="0 0 14 14"><circle cx="7" cy="7" r="7" fill="var(--accent-red)"/><path d="M4.5 3.5l1.6 1.8-.8 1a5 5 0 002.4 2.4l1-.8 1.8 1.6-1 1.1c-3 0-6-3-6-6z" fill="#fff"/></svg>
        616 555 0148
      </li>
      <li>
        <svg class="icon" viewBox="0 0 14 14"><circle cx="7" cy="7" r="7" fill="var(--accent-red)"/><rect x="4.8" y="3" width="4.4" height="8" rx="1" fill="#fff"/></svg>
        616 555 0148
      </li>
      <li>
        <svg class="icon" viewBox="0 0 14 14"><circle cx="7" cy="7" r="7" fill="var(--accent-red)"/><rect x="3.5" y="4.5" width="7" height="5" fill="#fff"/><path d="M3.5 4.5L7 7.3l3.5-2.8" stroke="var(--accent-red)" stroke-width=".9" fill="none"/></svg>
        Marcus@ferrickmail.com
      </li>
      <li>
        <svg class="icon" viewBox="0 0 14 14"><circle cx="7" cy="7" r="7" fill="var(--accent-red)"/><circle cx="7" cy="7" r="3.6" stroke="#fff" stroke-width="1" fill="none"/><path d="M3.4 7h7.2M7 3.4c-2 2.2-2 5 0 7.2M7 3.4c2 2.2 2 5 0 7.2" stroke="#fff" stroke-width=".8" fill="none"/></svg>
        www.hmferrickandsons.com
      </li>
      <li>
        <svg class="icon" viewBox="0 0 14 14"><circle cx="7" cy="7" r="7" fill="var(--accent-red)"/><path d="M7 11s-3-3.2-3-5.2a3 3 0 016 0C10 7.8 7 11 7 11z" fill="#fff"/><circle cx="7" cy="5.8" r="1.1" fill="var(--accent-red)"/></svg>
        418 Larkspur Street NE
      </li>
      <li class="address-line">Unit 12, Brookhaven, MI 49021</li>
    </ul>
  </section>

  <section class="card card--front" role="img" aria-label="Card front on a polished terrazzo concrete surface">
    <div class="card-front__brand">HMF</div>
    <span class="card-front__rule card-front__rule--left"></span>
    <div class="card-front__name">H M FERRICK &amp; SONS LTD</div>
    <span class="card-front__rule card-front__rule--right"></span>
    <div class="card-front__trade">CONCRETE CONTRACTORS</div>
    <div class="card-front__tagline">Specializing in concrete floor-finishing</div>
  </section>

</main>
</body>
</html>
```